Outdoor Sign - Slight Redesign

We are wanting to redesign our outdoor sign. Do not change the logos. The background images behind the Valcore and Brannick are a bit off and we would like different options. Wanting to display professionalism and boldness.

Target Market(s)

Oil and gas

Industry/Entity Type

Oil and gas

Requirements
Must have
• Use the same logo I uploaded. Please adjust the background image.
Should not have
• Do not start something new. Use what I have

```html
<!DOCTYPE html>
<html lang="en">
<head>
<meta charset="utf-8">
<title>Valcore &amp; Brannick Outdoor Sign</title>
<link href="https://fonts.googleapis.com/css2?family=Montserrat:wght@500;600;700;800&display=swap" rel="stylesheet">
<style>
  :root {
    --canvas: #cfcfcf;
    --ink: #0b0b0b;
    --silk-dark: #050505;
    --silk-mid: #3a3d42;
    --silk-light: #8d939b;
    --gold: #e6d386;
    --tan: #e0c49a;
    --bronze: #a48d6a;
    --white: #ffffff;
  }
  * { margin: 0; padding: 0; box-sizing: border-box; }
  html, body { width: 1111px; height: 1200px; overflow: hidden; }
  body {
    background: var(--canvas);
    font-family: "Montserrat", Arial, sans-serif;
    position: relative;
  }
  .sign {
    position: absolute;
    left: 115px;
    top: 380px;
    width: 880px;
    height: 440px;
    background: var(--ink);
    overflow: hidden;
  }
  .sign__art { position: absolute; inset: 0; width: 880px; height: 327px; }
  .brand {
    position: absolute;
    display: flex;
    align-items: center;
    gap: 14px;
    color: var(--white);
    font-weight: 800;
    letter-spacing: 1px;
  }
  .brand--valcore { left: 80px; top: 136px; font-size: 46px; }
  .brand--brannick { left: 530px; top: 196px; font-size: 44px; color: var(--gold); }
  .brand__mark--square { width: 36px; height: 36px; background: var(--tan); }
  .brand__mark--circle { width: 40px; height: 40px; border-radius: 50%; background: var(--bronze); }
  .contact-band {
    position: absolute;
    left: 0; top: 327px;
    width: 880px; height: 113px;
    background: var(--gold);
  }
  .contact-band__address {
    position: absolute;
    top: 10px; left: 0; width: 100%;
    text-align: center;
    font-size: 36px;
    font-weight: 500;
    color: var(--ink);
    letter-spacing: -0.5px;
  }
  .contact-band__phone {
    position: absolute;
    top: 52px; left: 0; width: 100%;
    text-align: center;
    font-size: 45px;
    font-weight: 700;
    color: var(--ink);
  }
  .rules { position: absolute; top: 54px; width: 190px; height: 40px; }
  .rules--left { left: 21px; }
  .rules--right { right: 21px; }
</style>
</head>
<body>
  <section class="sign" aria-label="Outdoor sign">
    <svg class="sign__art" viewBox="0 0 880 327" xmlns="http://www.w3.org/2000/svg">
      <defs>
        <linearGradient id="silkGradient" x1="0" y1="0" x2="1" y2="1">
          <stop offset="0" stop-color="var(--silk-dark)"/>
          <stop offset="0.3" stop-color="var(--silk-mid)"/>
          <stop offset="0.5" stop-color="var(--silk-dark)"/>
          <stop offset="0.72" stop-color="var(--silk-light)" stop-opacity="0.6"/>
          <stop offset="1" stop-color="var(--silk-dark)"/>
        </linearGradient>
      </defs>
      <rect class="silk-backdrop" width="880" height="327" fill="url(#silkGradient)" role="img" aria-label="Dark flowing silk background photograph"/>
      <path class="divider-stripe" d="M524 0 L535 0 L422 327 L380 327 Q405 320 415 300 Z" fill="var(--gold)"/>
      <path class="panel-right-shade" d="M535 0 L880 0 L880 327 L422 327 Z" fill="var(--silk-dark)" opacity="0.35"/>
    </svg>

    <div class="brand brand--valcore">
      <span class="brand__mark brand__mark--square"></span>
      <span class="brand__name">VALCORE</span>
    </div>
    <div class="brand brand--brannick">
      <span class="brand__mark brand__mark--circle"></span>
      <span class="brand__name">BRANNICK</span>
    </div>

    <div class="contact-band">
      <p class="contact-band__address">4820 WEST COUNTY ROAD 61</p>
      <svg class="rules rules--left" viewBox="0 0 190 40" xmlns="http://www.w3.org/2000/svg">
        <rect x="0" y="0" width="70" height="7" fill="var(--white)"/>
        <rect x="0" y="15" width="190" height="7" fill="var(--white)"/>
        <rect x="0" y="30" width="190" height="7" fill="var(--white)"/>
      </svg>
      <p class="contact-band__phone">(555) 014 2786</p>
      <svg class="rules rules--right" viewBox="0 0 190 40" xmlns="http://www.w3.org/2000/svg">
        <rect x="120" y="0" width="70" height="7" fill="var(--white)"/>
        <rect x="0" y="15" width="190" height="7" fill="var(--white)"/>
        <rect x="0" y="30" width="190" height="7" fill="var(--white)"/>
      </svg>
    </div>
  </section>
</body>
</html>
```